Business Card Design Project

We are a innovative residential building company based in Sydney, Australia
our business name is MORWEN CRAFTWORKS SOLUTIONS PTY LTD.
Our company by line (please incorporate) "Our Business is Building!"
We specialise in creating high end innovative residential Alterations & Additions for our clients.
We would like to see original high end designs that are professional, striking, creative & have the WOW factor...
We like BLACK, BLUE, ORANGE, WHITE, SILVER... We would like to convey to our clients - professionalism/innovative approach/design/creativity/assurance/wow factor...

Target Market(s)

Clients who want/need residential alterations or additions to their homes.

Industry/Entity Type

Residential

Requirements
Must have
• LOGO
Bi Line (somewhere)
Name
Title
Phone number
Email address

Member of the NHG (Northern Homecraft Guild) Logo
Web Address - www.morwencraftworks.com.au

Nice to have
• Fantail's are a small New Zealand bird and we would like to incorporate this as part of our new companies (double sided) business card. Whether it be the bird or just it's (fan) tail!
Should not have
• anything old-style.
we are looking for a contemporary, modern & striking Business Cards
clear strong colour accents
we had some stunning designs sent through, our favourites used the birds tail as an imprint on the card (not sure if that is clear of not)

```html
<!DOCTYPE html>
<html lang="en">
<head>
<meta charset="utf-8">
<title>Morwen Craftworks Solutions – Business Card</title>
<link rel="stylesheet" href="https://fonts.googleapis.com/css2?family=Questrial&display=swap">
<style>
  :root {
    --backdrop: #5e5e5e;
    --card-light: #fbfbf8;
    --card-mid: #ecece8;
    --card-edge: #d6d6d1;
    --ink: #2b2b2b;
    --ink-soft: #4a4a4a;
    --mark: #c9cbbd;
  }
  * { box-sizing: border-box; margin: 0; padding: 0; }
  html, body {
    width: 1200px;
    height: 1200px;
    overflow: hidden;
    background: var(--backdrop);
  }
  .canvas {
    position: relative;
    width: 1200px;
    height: 1200px;
    font-family: "Questrial", sans-serif;
    color: var(--ink);
    text-transform: uppercase;
  }
  .card {
    position: absolute;
    left: 150px;
    width: 900px;
    height: 514px;
    overflow: hidden;
    box-shadow: 0 6px 18px rgba(0,0,0,0.35);
  }
  .card--front { top: 60px; }
  .card--back  { top: 626px; }
  .fold-pattern {
    position: absolute;
    inset: 0;
    background: radial-gradient(ellipse at 45% 55%, var(--card-light) 0%, var(--card-mid) 55%, var(--card-edge) 100%);
  }
  .content { position: absolute; inset: 0; }

  /* front */
  .front-title {
    position: absolute;
    left: 250px;
    top: 200px;
    text-align: right;
    white-space: nowrap;
  }
  .front-title__name {
    font-size: 34px;
    font-weight: 400;
    letter-spacing: 5px;
  }
  .front-title__sub {
    font-size: 13px;
    letter-spacing: 2px;
    color: var(--ink-soft);
    margin-top: 14px;
    margin-right: 5px;
  }

  /* back */
  .company {
    position: absolute;
    left: 40px;
    top: 44px;
    letter-spacing: 2px;
  }
  .company__name { font-size: 20px; }
  .company__legal { font-size: 16px; color: var(--ink-soft); margin-top: 4px; }

  .person {
    position: absolute;
    right: 50px;
    top: 150px;
    text-align: right;
    letter-spacing: 3px;
  }
  .person__name { font-size: 28px; }
  .person__title { font-size: 17px; color: var(--ink-soft); margin-top: 6px; margin-right: 16px; }

  .brand-mark {
    position: absolute;
    left: 380px;
    top: 240px;
    display: flex;
    align-items: center;
    gap: 10px;
    font-size: 16px;
    letter-spacing: 3px;
    color: var(--ink-soft);
  }
  .brand-mark__dot {
    width: 18px;
    height: 18px;
    border-radius: 50%;
    background: var(--mark);
  }

  .byline {
    position: absolute;
    left: 40px;
    top: 390px;
    font-size: 15px;
    letter-spacing: 2px;
    color: var(--ink-soft);
  }

  .contact {
    position: absolute;
    left: 400px;
    top: 330px;
    font-size: 19px;
    letter-spacing: 2px;
    line-height: 1.45;
    border-collapse: collapse;
  }
  .contact__label { width: 44px; padding-right: 8px; }
</style>
</head>
<body>
<main class="canvas">

  <section class="card card--front" aria-label="Card front">
    <div class="fold-pattern" role="img" aria-label="Embossed pattern of radiating folds in silver white"></div>
    <div class="content">
      <div class="front-title">
        <h1 class="front-title__name">Morwen Craftworks</h1>
        <p class="front-title__sub">Solutions</p>
      </div>
    </div>
  </section>

  <section class="card card--back" aria-label="Card back">
    <div class="fold-pattern" role="img" aria-label="Embossed pattern of radiating folds in silver white"></div>
    <div class="content">
      <div class="company">
        <p class="company__name">Morwen Craftworks</p>
        <p class="company__legal">Solutions Pty Ltd</p>
      </div>

      <div class="person">
        <p class="person__name">Tomas Reyne</p>
        <p class="person__title">Manager</p>
      </div>

      <div class="brand-mark">
        <span class="brand-mark__dot"></span>
        <span>Morwen</span>
      </div>

      <p class="byline">Our Business is Building</p>

      <table class="contact">
        <tr><td class="contact__label">P:</td><td>0061829475</td></tr>
        <tr><td class="contact__label">W:</td><td>www.morwencraftworks.com</td></tr>
        <tr><td class="contact__label">E:</td><td>tomasreyne@morwen.com</td></tr>
        <tr><td class="contact__label">A:</td><td>XYZ Address</td></tr>
      </table>
    </div>
  </section>

</main>
</body>
</html>
```